Creative Photography Business Card

Looking for a unique, creative, elegant, sophisticated and professional business card for my photography business.

I specialise in children, families, modelling, weddings and special event photography

Things to include:
Logo - will attach
Email: hello@mirabellwoodsphoto.com.au
web:www.mirabellwoodsphoto.com.au
Ph: 0438 502 671

I will also upload some of my work that you may like to use.

Please be creative and unique in your designs.

```html
<!DOCTYPE html>
<html lang="en">
<head>
<meta charset="utf-8">
<title>Mirabell Woods Photography – Business Card</title>
<link href="https://fonts.googleapis.com/css2?family=Lato:wght@400;700&display=swap" rel="stylesheet">
<style>
  :root {
    --brand-blue: #2a66a8;
    --ink-blue: #1f5592;
    --paper: #ffffff;
    --stage: #e9ebee;
    --photo-warm: #d9b49a;
    --photo-green: #8fa86e;
    --photo-stone: #c8c2b6;
    --photo-orange: #e99a5a;
    --photo-sky: #c9d6e0;
  }
  * { margin: 0; padding: 0; box-sizing: border-box; }
  html, body { width: 1200px; height: 926px; overflow: hidden; }
  body {
    background: var(--stage);
    font-family: "Lato", sans-serif;
    display: flex;
    flex-direction: column;
    align-items: center;
    justify-content: center;
    gap: 40px;
  }
  .card {
    width: 720px;
    height: 411px;
    position: relative;
    box-shadow: 0 6px 18px rgba(0,0,0,.18);
    overflow: hidden;
  }
  /* Front side */
  .card-front {
    background: var(--brand-blue);
    padding: 22px;
  }
  .card-front .inner {
    background: var(--paper);
    width: 100%;
    height: 100%;
    position: relative;
  }
  .brand-mark {
    position: absolute;
    top: 70px;
    left: 50%;
    transform: translateX(-50%);
    display: flex;
    align-items: center;
    gap: 14px;
    color: var(--ink-blue);
    font-weight: 700;
    font-size: 30px;
    white-space: nowrap;
  }
  .brand-mark .dot {
    width: 26px;
    height: 26px;
    border-radius: 50%;
    border: 3px solid var(--ink-blue);
  }
  .contact {
    position: absolute;
    top: 200px;
    left: 0;
    right: 0;
    text-align: center;
    color: var(--ink-blue);
    font-size: 19px;
    line-height: 1.55;
  }
  .contact .label { font-weight: 700; }
  /* Back side */
  .card-back svg { display: block; }
  .back-brand {
    position: absolute;
    left: 34px;
    bottom: 44px;
    color: var(--paper);
    font-weight: 700;
    font-size: 17px;
    display: flex;
    align-items: center;
    gap: 8px;
    white-space: nowrap;
  }
  .back-brand .dot {
    width: 16px;
    height: 16px;
    border-radius: 50%;
    border: 2px solid var(--paper);
  }
</style>
</head>
<body>

  <section class="card card-front" aria-label="Business card front">
    <div class="inner">
      <div class="brand-mark"><span class="dot"></span>Mirabell Woods Photography</div>
      <div class="contact">
        <p><span class="label">phone:</span> 0438 502 671</p>
        <p><span class="label">web:</span> www.mirabellwoodsphoto.com.au</p>
        <p><span class="label">email:</span> hello@mirabellwoodsphoto.com.au</p>
      </div>
    </div>
  </section>

  <section class="card card-back" aria-label="Business card back">
    <svg width="720" height="411" viewBox="0 0 720 411" xmlns="http://www.w3.org/2000/svg">
      <polygon role="img" aria-label="Photo of a smiling young child" points="0,0 150,0 0,150" fill="var(--photo-warm)"/>
      <polygon role="img" aria-label="Wedding photo of a couple kissing" points="150,0 300,0 0,300 0,150" fill="var(--photo-green)"/>
      <polygon role="img" aria-label="Family group portrait outdoors" points="300,0 460,0 100,360 0,360 0,300" fill="var(--photo-sky)"/>
      <polygon role="img" aria-label="Portrait of a young woman resting her chin on her hands" points="460,0 600,0 210,411 100,411 100,360" fill="var(--photo-stone)"/>
      <polygon role="img" aria-label="Close-up portrait of two smiling children" points="600,0 720,0 720,411 210,411" fill="var(--photo-orange)"/>
      <polygon points="0,230 230,230 60,411 0,411" fill="var(--brand-blue)"/>
    </svg>
    <div class="back-brand"><span class="dot"></span>Mirabell Woods</div>
  </section>

</body>
</html>
```